New Bicycle shop business card

Hi!
I'm looking for a business card for my new proffesional bike mechanics shop. This shop is only for fixing broken bikes and not selling bikes.
Peferbly a modern and sleek and modern design.
Colors: black, grey, red, white
Information:
Name: Rijwielwerkplaats Vanhoutem
Shop owner: Bart Vanhoutem & Sanne Maertens
Website: www.rijwielwerkplaats-vanhoutem.be
Email: info@rijwielwerkplaats-vanhoutem.be
Phone number: +32471902386
Street adres: Kerkweg 64
9970 Oostmoere
Slogan/shop information: Herstellingen van alle merken.
Logo: see files.
Target Market(s)
People who seek a mechanic to fix or upgrade their bikes.
Contact Information for Business Card
Information:
Website: info@rijwielwerkplaats-vanhoutem.be
9970 Oostmoere
Logo: see files.

```html
<!DOCTYPE html>
<html lang="nl">
<head>
<meta charset="utf-8">
<title>Rijwielwerkplaats Vanhoutem – Visitekaartje</title>
<link rel="stylesheet" href="https://fonts.googleapis.com/css2?family=Montserrat:wght@500;700;800&family=Questrial&display=swap">
<style>
  :root {
    --red: #d81f4f;
    --red-deep: #b8143d;
    --black: #0b0b0b;
    --white: #ffffff;
    --paper: #f3f3f3;
    --grey: #8d8d8d;
    --stage: #e7e5e2;
  }
  * { box-sizing: border-box; margin: 0; padding: 0; }
  html, body { width: 1200px; height: 780px; overflow: hidden; }
  body { background: var(--stage); position: relative; font-family: "Questrial", "Century Gothic", sans-serif; }

  .card { position: absolute; border-radius: 18px; overflow: hidden; box-shadow: 0 10px 30px rgba(0,0,0,.18); }

  /* Front – portrait */
  .card-front { left: 90px; top: 75px; width: 380px; height: 630px; background: linear-gradient(#ffffff, #ececec 45%); }
  .card-front .backdrop { position: absolute; inset: 0; }
  .brand { position: absolute; top: 46px; left: 0; right: 0; text-align: center; }
  .brand-dot { display: block; width: 58px; height: 58px; border-radius: 50%; background: var(--red); margin: 0 auto 18px; }
  .brand-name { font-family: "Montserrat", sans-serif; font-weight: 800; color: var(--black); font-size: 22px; letter-spacing: 1.5px; line-height: 1.25; text-transform: uppercase; }
  .owners { position: absolute; top: 298px; left: 0; right: 0; text-align: center; color: var(--white); font-size: 13.5px; letter-spacing: .6px; text-transform: uppercase; }
  .contact { position: absolute; left: 20px; right: 20px; text-align: center; color: var(--white); font-size: 14px; }
  .contact .rule { position: relative; height: 34px; }
  .contact .rule::before, .contact .rule::after { content: ""; position: absolute; top: 17px; width: 110px; height: 2px; background: var(--red); }
  .contact .rule::before { left: 10px; }
  .contact .rule::after { right: 10px; }
  .contact .icon { position: absolute; left: 50%; top: 0; transform: translateX(-50%); width: 34px; height: 34px; }
  .contact .value { margin-top: 6px; display: block; }
  .contact-phone { top: 340px; }
  .contact-mail { top: 410px; }
  .contact-address { top: 480px; }
  .website { position: absolute; left: 0; right: 0; bottom: 22px; text-align: center; color: var(--white); font-size: 14px; letter-spacing: .3px; }

  /* Back – landscape */
  .card-back { left: 520px; top: 200px; width: 600px; height: 380px; background: radial-gradient(ellipse at 60% 40%, #e3285a, var(--red) 45%, var(--red-deep)); color: var(--white); }
  .back-brand { position: absolute; left: 0; right: 0; top: 110px; text-align: center; }
  .back-brand .brand-dot { background: var(--white); width: 62px; height: 62px; margin-bottom: 20px; }
  .back-brand .brand-name { color: var(--white); font-size: 28px; letter-spacing: 2px; }
  .slogan { position: absolute; left: 0; right: 0; bottom: 70px; text-align: center; font-size: 17px; letter-spacing: .5px; }
</style>
</head>
<body>

<article class="card card-front">
  <svg class="backdrop" viewBox="0 0 380 630" width="380" height="630" aria-hidden="true">
    <path d="M0 222 Q200 222 380 300 L380 630 L0 630 Z" fill="#d81f4f"/>
    <path d="M0 232 Q200 232 380 312 L380 630 L0 630 Z" fill="#0b0b0b"/>
    <path d="M150 250 Q290 262 380 318" fill="none" stroke="#ffffff" stroke-width="2" opacity=".85"/>
    <rect x="0" y="560" width="380" height="70" fill="#d81f4f"/>
    <rect x="0" y="556" width="380" height="4" fill="#ffffff"/>
  </svg>

  <header class="brand">
    <span class="brand-dot"></span>
    <p class="brand-name">Rijwielwerkplaats<br>Vanhoutem</p>
  </header>

  <p class="owners">Bart Vanhoutem &amp; Sanne Maertens</p>

  <div class="contact contact-phone">
    <div class="rule">
      <svg class="icon" viewBox="0 0 34 34" aria-hidden="true"><circle cx="17" cy="17" r="15" fill="#fff" stroke="#0b0b0b" stroke-width="2"/><path d="M13 10 l3 4 -2 2 q2 4 5 5 l2-2 4 3 -2 3 q-9-1-12-12z" fill="#0b0b0b"/></svg>
    </div>
    <span class="value">+32471902386</span>
  </div>

  <div class="contact contact-mail">
    <div class="rule">
      <svg class="icon" viewBox="0 0 34 34" aria-hidden="true"><circle cx="17" cy="17" r="15" fill="#fff" stroke="#0b0b0b" stroke-width="2"/><rect x="9" y="12" width="16" height="11" fill="none" stroke="#0b0b0b" stroke-width="2"/><path d="M9 12 l8 6 8-6" fill="none" stroke="#0b0b0b" stroke-width="2"/></svg>
    </div>
    <span class="value">info@rijwielwerkplaats-vanhoutem.be</span>
  </div>

  <div class="contact contact-address">
    <div class="rule">
      <svg class="icon" viewBox="0 0 34 34" aria-hidden="true"><circle cx="17" cy="17" r="15" fill="#fff" stroke="#0b0b0b" stroke-width="2"/><path d="M17 26 q-7-8-7-12 a7 7 0 0 1 14 0 q0 4-7 12z" fill="#0b0b0b"/><circle cx="17" cy="14" r="2.5" fill="#fff"/></svg>
    </div>
    <span class="value">Kerkweg 64, 9970 Oostmoere</span>
  </div>

  <p class="website">www.rijwielwerkplaats-vanhoutem.be</p>
</article>

<article class="card card-back">
  <header class="back-brand brand">
    <span class="brand-dot"></span>
    <p class="brand-name">Rijwielwerkplaats Vanhoutem</p>
  </header>
  <p class="slogan">Herstellingen Van Alle Merken</p>
</article>

</body>
</html>
```